International Petrochemical business needs a web design for Clearway Desk system

We need a web design for a "Clearway Desk" system for an international petrochemical company. The web site is used internally within the company. It is hosted by an internal department which provides government permit request service for other departments.

We would like to see designs of two pages using color light blue. (home page, internal page as attached).
Home Page:
1. Header has a background image and small animation. Header on home page can be taller than the header of the internal page.
2. Layout as attached.

Internal Page:
1. Header can use the same background image as the home page and can be shorter to utilize the page for content.
2. The blue icon behind every captions represent an icon. When user move mouse over this icon, it displays the caption in Thai language as a tooltip. This icon needs to be redesign.

The final design should communicate the followings:
- Excellent service provided system in terms of time and accurary
- Rapid growth of business via building petrochemical refinery plant

For Internal Page, the blue circle behind every captions represent an icon. When mouse over this icon, a tool tip showing the caption in Thai language is shown. Please also design this icon..

There are more feedbacks from customer as followed:

1. Banner should consists of 
    1.1 "Approved" stamp on paper
    1.2 An image of Garuda. It is used on every government documents in Thailand
    1.3 Image of petrochemical plant
2. Each menu item (Home, Permit, Search, etc) should have different colors. Drop down menu will use the same color as its parent menu item.
3. Overall tone of the web page should be light blue with background of the body the web page in white
4. "New Request" button should use green color with icon on it
5. Table header of each box in the body of the page should use dark blue background with text in white

Please kindly submit your revisions.
Thank you.

Reason: We get some late feedbacks from customers which was just updated to all designers.

• 1. Design for 1024x768 screen resolution
2. Use light blue theme
3. Background of header where the Meridian Petrochem is must have white background

```html
<!DOCTYPE html>
<html lang="en">
<head>
<meta charset="utf-8">
<title>Clearway Desk</title>
<link rel="stylesheet" href="https://fonts.googleapis.com/css2?family=Open+Sans:wght@400;600;700&family=Sarabun:wght@400&display=swap">
<style>
  :root {
    --sky: #93d2f3;
    --sky-deep: #4a8db8;
    --nav-home: #3f7fb8;
    --nav-permits: #2f9a8f;
    --nav-search: #5a6fc0;
    --nav-report: #7a5aa8;
    --nav-admin: #c07a2c;
    --nav-help: #3a9a4c;
    --panel-top: #7889a8;
    --panel-bottom: #4a5a78;
    --thead-top: #34486e;
    --thead-bottom: #243657;
    --white: #ffffff;
    --panel-bg: #f7f7f7;
    --panel-line: #dcdcdc;
    --text: #3a3a3a;
    --link: #1f5fa8;
    --green-top: #a6dd5c;
    --green-bottom: #76b82a;
    --green-text: #2d4a12;
    --footer: #4a4a4a;
    --dot-red: #e02a2a;
    --dot-yellow: #f2c515;
  }
  * { box-sizing: border-box; margin: 0; padding: 0; }
  html, body { width: 1200px; height: 1143px; overflow: hidden; }
  body {
    font-family: "Open Sans", Arial, sans-serif;
    color: var(--text);
    background: linear-gradient(180deg, var(--sky-deep) 0, #6fb4df 60px, var(--sky) 120px, var(--sky) 100%);
    position: relative;
  }
  .site-header { position: absolute; left: 0; top: 0; width: 1200px; height: 87px; }
  .site-header::before {
    content: ""; position: absolute; left: 110px; top: -40px; width: 240px; height: 150px;
    background: radial-gradient(ellipse at center, rgba(255,255,255,.95) 0, rgba(255,255,255,.6) 40%, rgba(255,255,255,0) 70%);
  }
  .brand {
    position: absolute; left: 163px; top: 22px; width: 140px;
    font-size: 20px; font-weight: 700; line-height: 23px; color: #3f7fae; text-align: center;
  }
  .system-title {
    position: absolute; left: 438px; top: 36px;
    font-size: 25px; font-weight: 600; color: var(--white);
  }
  .main-nav {
    position: absolute; left: 110px; top: 87px; width: 981px; height: 43px;
    display: flex; border-radius: 4px 4px 0 0; overflow: hidden;
  }
  .main-nav a {
    flex: 1; display: flex; align-items: center; justify-content: center; gap: 6px;
    color: var(--white); text-decoration: none; font-size: 17px;
    background-image: linear-gradient(180deg, rgba(255,255,255,.18), rgba(0,0,0,.12));
    border-right: 1px solid rgba(0,0,0,.18);
  }
  .main-nav a:last-child { border-right: 0; }
  .nav-home { background-color: var(--nav-home); }
  .nav-permits { background-color: var(--nav-permits); }
  .nav-search { background-color: var(--nav-search); }
  .nav-report { background-color: var(--nav-report); }
  .nav-admin { background-color: var(--nav-admin); }
  .nav-help { background-color: var(--nav-help); }
  .caret { width: 0; height: 0; border-left: 4px solid transparent; border-right: 4px solid transparent; border-top: 5px solid var(--white); }
  .page {
    position: absolute; left: 110px; top: 130px; width: 981px; height: 952px;
    background: var(--white); padding: 20px 21px;
  }
  .banner {
    height: 170px; border-radius: 7px;
    background: radial-gradient(ellipse at 50% 45%, #f4b14a 0, #b06a22 18%, #3e3a26 45%, #1d2226 100%);
  }
  .grid { display: grid; grid-template-columns: 459px 459px; column-gap: 21px; margin-top: 21px; }
  .panel {
    background: var(--panel-bg); border: 1px solid var(--panel-line); border-radius: 5px;
    position: relative; overflow: hidden;
  }
  .panel-title {
    height: 34px; padding-left: 12px; display: flex; align-items: center;
    background: linear-gradient(180deg, var(--panel-top), var(--panel-bottom));
    color: var(--white); font-size: 16px; font-weight: 600;
  }
  .data-table { width: calc(100% - 14px); margin: 6px 7px 0; border-collapse: collapse; font-size: 13.5px; }
  .data-table th {
    background: linear-gradient(180deg, var(--thead-top), var(--thead-bottom));
    color: var(--white); font-weight: 600; font-size: 13px;
    text-align: left; height: 31px; padding: 0 7px; border-right: 1px solid #4e6288;
  }
  .data-table th:last-child { border-right: 0; }
  .data-table td { height: 31px; padding: 0 7px; border-bottom: 1px solid var(--panel-line); }
  .data-table a { color: var(--link); }
  .thai { font-family: "Sarabun", "Open Sans", sans-serif; font-size: 14px; }
  .num { text-align: right; padding-right: 12px !important; }
  .center { text-align: center; }
  .dot { display: inline-block; width: 11px; height: 11px; border-radius: 50%; margin-left: 4px; vertical-align: -1px; }
  .dot.red { background: radial-gradient(circle at 35% 35%, #ff8a8a, var(--dot-red) 60%); }
  .dot.yellow { background: radial-gradient(circle at 35% 35%, #fff29a, var(--dot-yellow) 60%); }
  .pager { position: absolute; left: 0; right: 0; bottom: 4px; display: flex; justify-content: center; gap: 3px; }
  .pager span {
    width: 20px; height: 24px; border: 1px solid #c8c8c8; border-radius: 3px; background: #ededed;
    font-size: 13px; display: flex; align-items: center; justify-content: center; color: #555;
  }
  .pager .arrow {
    width: 26px; border: 0; border-radius: 5px; color: var(--white); font-size: 16px; font-weight: 700;
    background: linear-gradient(180deg, #6d7e9c, #3e4d69);
  }
  .wide { grid-column: 1 / 3; margin-top: 20px; }
  .side { display: flex; flex-direction: column; gap: 19px; margin-top: 22px; }
  .btn-new {
    height: 53px; border-radius: 5px; border: 1px solid #6ea52c;
    background: linear-gradient(180deg, var(--green-top), var(--green-bottom));
    display: flex; align-items: center; justify-content: center; gap: 10px;
    color: var(--green-text); font-size: 16.5px; font-weight: 600; text-decoration: none;
  }
  .btn-icon { width: 22px; height: 22px; }
  .site-footer {
    position: absolute; left: 110px; top: 1082px; width: 981px; height: 40px;
    background: var(--footer); border-radius: 0 0 4px 4px;
    color: var(--white); font-size: 16px; font-weight: 600;
    display: flex; align-items: center; justify-content: center;
  }
</style>
</head>
<body>
  <header class="site-header">
    <div class="brand">Meridian Petrochem</div>
    <div class="system-title">Clearway Desk</div>
  </header>

  <nav class="main-nav">
    <a href="#" class="nav-home">Home</a>
    <a href="#" class="nav-permits">Permits <i class="caret"></i></a>
    <a href="#" class="nav-search">Search</a>
    <a href="#" class="nav-report">Report</a>
    <a href="#" class="nav-admin">Admin</a>
    <a href="#" class="nav-help">Help</a>
  </nav>

  <main class="page">
    <div class="banner" role="img" aria-label="Petrochemical refinery plant at sunset with pipelines"></div>

    <div class="grid">
      <section class="panel" style="height:233px">
        <h2 class="panel-title">New Requests</h2>
        <table class="data-table">
          <tr><th style="width:106px">Request No.</th><th style="width:149px">Requested Date</th><th>Branch</th></tr>
          <tr><td><a href="#">56-0003</a></td><td>20/4/2013</td><td>GC1</td></tr>
          <tr><td><a href="#">56-0004</a></td><td>20/4/2013</td><td>GC2</td></tr>
        </table>
        <div class="pager"><span class="arrow">‹</span><span>1</span><span>2</span><span>3</span><span>4</span><span class="arrow">›</span></div>
      </section>

      <section class="panel" style="height:233px">
        <h2 class="panel-title">My Working Requests</h2>
        <table class="data-table">
          <tr><th style="width:106px">Request No.</th><th style="width:119px">Requested Date</th><th>Status</th></tr>
          <tr><td><a href="#">55-0200</a></td><td>20/4/2013</td><td>Waiting for process</td></tr>
          <tr><td><a href="#">55-0210</a></td><td>20/4/2013</td><td>In progress</td></tr>
          <tr><td><a href="#">55-0300</a></td><td>20/4/2013</td><td>Incomplete document</td></tr>
          <tr><td><a href="#">55-0301</a></td><td>20/4/2013</td><td>Cancel requested</td></tr>
        </table>
        <div class="pager"><span class="arrow">‹</span><span>1</span><span>2</span><span>3</span><span>4</span><span class="arrow">›</span></div>
      </section>

      <section class="panel wide" style="height:171px">
        <h2 class="panel-title">Expiring Permits</h2>
        <table class="data-table">
          <tr><th style="width:116px">Permit No</th><th style="width:120px">Expire Date</th><th style="width:251px">Permit Name</th><th style="width:120px">Branch</th><th style="width:155px">Required Time (Day)</th><th>Required Time (Day)</th></tr>
          <tr><td><a href="#">AB56001</a></td><td>25/3/2013</td><td>Permit Name ###10</td><td>GC1</td><td class="num">30 <i class="dot red"></i></td><td class="center">-40</td></tr>
          <tr><td><a href="#">BIO5502</a></td><td>24/3/2013</td><td>Permit Name ###20</td><td>GC2</td><td class="num">60 <i class="dot yellow"></i></td><td class="center">15</td></tr>
        </table>
        <div class="pager"><span class="arrow">‹</span><span>1</span><span>2</span><span>3</span><span>4</span><span class="arrow">›</span></div>
      </section>

      <section class="panel" style="height:274px;margin-top:22px">
        <h2 class="panel-title">My In Progress Requests</h2>
        <table class="data-table">
          <tr><th style="width:106px">Request No.</th><th style="width:149px">Requested Date</th><th>Status</th></tr>
          <tr><td><a href="#">56-0003</a></td><td>20/4/2013</td><td class="thai">ระหว่างดำเนินการ</td></tr>
          <tr><td><a href="#">56-0004</a></td><td>20/4/2013</td><td class="thai">รอดำเนินการ</td></tr>
        </table>
        <div class="pager"><span class="arrow">‹</span><span>1</span><span>2</span><span>3</span><span>4</span><span class="arrow">›</span></div>
      </section>

      <div class="side">
        <a class="btn-new" href="#">
          <svg class="btn-icon" viewBox="0 0 22 22" aria-hidden="true">
            <circle cx="11" cy="11" r="10" fill="#ffffff" stroke="#5c9a1e" stroke-width="1.5"/>
            <path d="M11 6v10M6 11h10" stroke="#4f8a18" stroke-width="2.4" stroke-linecap="round"/>
          </svg>
          New Request
        </a>
        <section class="panel" style="height:202px">
          <h2 class="panel-title">Recent Completed Requests</h2>
          <table class="data-table">
            <tr><th style="width:137px">Request No.</th><th>Completed Date</th></tr>
            <tr><td><a href="#">55-0100</a></td><td>20/4/2013</td></tr>
            <tr><td><a href="#">55-0088</a></td><td>20/4/2013</td></tr>
            <tr><td><a href="#">55-0002</a></td><td>20/4/2013</td></tr>
          </table>
          <div class="pager"><span class="arrow">‹</span><span>1</span><span>2</span><span>3</span><span>4</span><span class="arrow">›</span></div>
        </section>
      </div>
    </div>
  </main>

  <footer class="site-footer">Image Footer</footer>
</body>
</html>
```